CRPG is needing business cards, and stationary created.

Pixel Forge created a logo for our business, and now we are wanting business cards, and stationary. I have included two designs of the same logo. Please feel free to use them as you want. The name of the company is Cedar Ridge Property Group LLC, the address is 812 NE Willow Ln., Suite 9, the city & state is Bend, Oregon, zip code is 97815, Telephone number is 541-327-4489, Fax number is 541-327-6051, the name on the business card is Carl Whitby CMCA

Industry/Entity Type

Property Management

Contact Information for Business Card

The card needs to look professional. Upscale.

Requirements
Must have
• The colors we are using are on the logo that has been uploaded.

```html
<!DOCTYPE html>
<html lang="en">
<head>
<meta charset="utf-8">
<title>Cedar Ridge Property Group – Business Card</title>
<link rel="stylesheet" href="https://fonts.googleapis.com/css2?family=Roboto:wght@400;500;700&display=swap">
<style>
  :root {
    --teal: #1f9483;
    --slate: #3e4a5b;
    --white: #ffffff;
    --paper: #eef0ef;
  }
  * { box-sizing: border-box; margin: 0; padding: 0; }
  html, body { width: 1200px; height: 1040px; overflow: hidden; }
  body {
    background: var(--paper);
    font-family: "Roboto", Arial, sans-serif;
    position: relative;
  }
  .card {
    position: absolute;
    left: 180px;
    width: 840px;
    height: 480px;
    border-radius: 30px;
    overflow: hidden;
    box-shadow: 0 10px 30px rgba(0,0,0,.18);
  }
  .card-front { top: 30px; background: var(--white); }
  .card-back { top: 540px; background: var(--teal); }
  .front-shapes { position: absolute; inset: 0; }

  .brand { position: absolute; color: var(--teal); }
  .brand-front { left: 50px; top: 180px; }
  .brand-row { display: flex; align-items: center; gap: 14px; }
  .brand-square { width: 30px; height: 30px; background: var(--slate); flex: none; }
  .brand-name {
    font-weight: 700; font-size: 56px; letter-spacing: 1px; line-height: 1; white-space: nowrap;
  }
  .brand-front .brand-name { font-size: 44px; }
  .brand-front .brand-square { width: 26px; height: 26px; }
  .brand-sub {
    margin-top: 8px; font-size: 13px; font-weight: 500;
    letter-spacing: 3px; color: var(--slate); padding-left: 44px;
  }
  .brand-front .brand-sub { padding-left: 40px; font-size: 12px; }
  .brand-tag {
    margin-top: 8px; display: flex; align-items: center; gap: 10px;
    font-size: 11px; letter-spacing: 7px; color: var(--slate); white-space: nowrap;
  }
  .brand-front .brand-tag { font-size: 10px; letter-spacing: 6px; }
  .brand-tag::before { content: ""; width: 30px; height: 1px; background: var(--slate); }

  .contact {
    position: absolute; right: 56px; top: 110px;
    color: var(--white); text-align: right;
  }
  .contact-name { font-size: 32px; font-weight: 700; margin-bottom: 22px; white-space: nowrap; }
  .contact-line {
    display: flex; justify-content: flex-end; align-items: center; gap: 10px;
    font-size: 19px; line-height: 1.6;
  }
  .contact-line svg { width: 16px; height: 16px; fill: var(--white); }
  .contact-address { margin-top: 18px; font-size: 19px; line-height: 1.5; }

  .brand-back { left: 90px; bottom: 80px; color: var(--white); }
  .brand-back .brand-square { background: var(--white); }
  .brand-back .brand-sub,
  .brand-back .brand-tag { color: var(--white); }
  .brand-back .brand-tag::before { background: var(--white); }
  .website { margin-top: 12px; font-size: 20px; color: var(--white); }
</style>
</head>
<body>

<section class="card card-front">
  <svg class="front-shapes" viewBox="0 0 840 480" width="840" height="480" aria-hidden="true">
    <path d="M480,0 C405,40 400,160 430,260 C465,380 420,460 300,480 L840,480 L840,0 Z" fill="var(--teal)"/>
    <path d="M230,480 C360,470 425,420 440,330 C445,420 390,468 290,480 Z" fill="var(--slate)"/>
  </svg>

  <div class="brand brand-front">
    <div class="brand-row">
      <span class="brand-square"></span>
      <span class="brand-name">CEDAR RIDGE</span>
    </div>
    <div class="brand-sub">PROPERTY GROUP</div>
    <div class="brand-tag">ROOTED IN SERVICE</div>
  </div>

  <div class="contact">
    <div class="contact-name">Carl Whitby CMCA</div>
    <div class="contact-line">541-327-4489
      <svg viewBox="0 0 24 24"><path d="M6.6 10.8a15 15 0 0 0 6.6 6.6l2.2-2.2c.3-.3.7-.4 1-.2 1.1.4 2.300.6 3.6.6.6 0 1 .4 1 1V20c0 .6-.4 1-1 1A17 17 0 0 1 3 4c0-.6.4-1 1-1h3.5c.6 0 1 .4 1 1 0 1.3.2 2.5.6 3.6.1.3 0 .7-.2 1z"/></svg>
    </div>
    <div class="contact-line">541-327-6051
      <svg viewBox="0 0 24 24"><path d="M6 2h10v5H6z M3 8h18v11H3z M7 15h10v7H7z"/></svg>
    </div>
    <div class="contact-address">812 NE Willow Ln., Suite 9<br>Bend, Oregon 97815</div>
  </div>
</section>

<section class="card card-back">
  <div class="brand brand-back">
    <div class="brand-row">
      <span class="brand-square"></span>
      <span class="brand-name">CEDAR RIDGE</span>
    </div>
    <div class="brand-sub">PROPERTY GROUP</div>
    <div class="brand-tag">ROOTED IN SERVICE</div>
    <div class="website">cedarridgepropertygroup.com</div>
  </div>
</section>

</body>
</html>
```